need web page design for BrightOakly.com

This site sells information products for international corporate users. It is selling Silver Pathways and Quarterly Ledger Craft, a product on international business tax, and other books. See sample. I will also upload a possible logo. Upload 2 The tag line is Predicting and Solving Business and Law Issues for the Multinational Upload 3 is a sample theme from Shopify, the site I will use. The sample is for ideas only. I am not wedded to it. Upload 4 is Meridian Ledger Journal Pge

Number of Pages Required

2 page

```html
<!DOCTYPE html>
<html lang="en">
<head>
<meta charset="utf-8">
<title>BrightOakly.com</title>
<link href="https://fonts.googleapis.com/css2?family=Noto+Serif:wght@400;700&family=Roboto+Condensed:wght@400;700&family=Open+Sans:wght@400;600&display=swap" rel="stylesheet">
<style>
:root{
  --navy:#0d2a7a;
  --ink:#222;
  --line:#d6d6d6;
  --footer-bg:#efefef;
  --nav-active:#e4e4e4;
  --orange:#e88a12;
  --red:#c8141b;
}
*{box-sizing:border-box;margin:0;padding:0}
html,body{width:798px;height:1200px;overflow:hidden;background:#fff}
body{position:relative;font-family:'Noto Serif',Georgia,serif;color:var(--ink)}
.abs{position:absolute}

/* header */
.search{left:40px;top:84px;width:158px;height:28px;border:1px solid #bbb;font-style:italic;font-size:10px;color:#777;padding:8px 7px}
.search svg{position:absolute;right:6px;top:5px}
.brand{left:0;width:798px;top:12px;text-align:center}
.brand-mark{display:inline-block;width:96px;height:96px;border-radius:50%;background:var(--navy)}
.brand-name{font-family:'Roboto Condensed',Arial,sans-serif;font-weight:700;font-size:33px;color:var(--navy);margin-top:6px;line-height:1}
.brand-tag{font-family:'Roboto Condensed',Arial,sans-serif;font-weight:400;font-size:10px;color:#555;margin-top:3px}
.cart{right:34px;top:88px;display:flex;align-items:flex-end;gap:8px;font-size:11.5px;text-transform:uppercase}

/* nav */
.nav{left:0;top:181px;width:798px;height:41px;border-top:1px solid var(--line);border-bottom:1px solid var(--line)}
.nav ul{list-style:none;display:flex;position:absolute;left:75px;top:0;height:40px}
.nav li{height:40px;line-height:40px;font-size:15px;color:#444;padding:0 19px;border-right:1px solid var(--line)}
.nav li:last-child{border-right:0}
.nav li.active{background:var(--nav-active);color:var(--navy)}

/* hero */
.hero{left:0;top:222px;width:798px;height:365px;background:linear-gradient(90deg,#f4f6f8 0%,#eef1f4 45%,#e3e7ec 100%)}
.hero-photo{left:300px;top:0;width:498px;height:365px;
  background:
    linear-gradient(180deg,rgba(244,246,248,0) 70%,#e4e8ed 100%),
    linear-gradient(90deg,rgba(238,241,244,1) 0%,rgba(238,241,244,0) 30%),
    linear-gradient(100deg,#efe9e4 20%,#e8d6c8 45%,#dcb7ad 65%,#d8c3c0 82%,#d3d9e0 100%)}
.hero h1{left:40px;top:74px;font-family:'Roboto Condensed',Arial,sans-serif;font-weight:700;font-size:31px;color:var(--navy)}
.hero p{left:40px;top:118px;font-weight:700;font-size:15px;line-height:23px;color:#111}
.hero-btn{left:41px;top:181px}

/* tabs */
.tabs{left:0;top:587px;width:798px;height:34px;border-bottom:1px solid var(--line);background:linear-gradient(#fff,#f5f5f5)}
.tab{top:0;height:34px;line-height:34px;font-size:12px;text-transform:uppercase;color:#555}
.tab.active{background:#fff;border:1px solid var(--line);border-bottom:1px solid #fff;color:#111;padding:0 11px;height:35px}

/* products */
.cover{top:652px;width:144px;height:200px;overflow:hidden}
.cover-1{left:83px;background:linear-gradient(#6e747b 0 28%,#5a6674 28%,#3c4955 65%,#2b3540 100%)}
.cover-1 .c-title{position:absolute;left:14px;top:8px;font-family:'Roboto Condensed',Arial,sans-serif;font-size:11.5px;line-height:13px;color:#eef0f2}
.cover-1 .c-author{position:absolute;right:6px;bottom:3px;font-family:'Roboto Condensed',Arial,sans-serif;font-size:11px;color:#dfe3e6}
.cover-2{left:246px;background:#f4f4f2}
.cover-2 .c-band{position:absolute;left:0;top:0;width:144px;height:20px;background:#1b3a8a;color:#fff;font-size:5.5px;letter-spacing:1px;text-transform:uppercase;text-align:center;line-height:20px}
.cover-2 .c-title{position:absolute;left:0;top:28px;width:144px;text-align:center;font-size:7px;line-height:11px;text-transform:uppercase;color:#555;letter-spacing:.3px}
.cover-2 .c-dark{position:absolute;left:0;top:69px;width:144px;height:131px;background:#1b1b1b;border-top:2px solid #888}
.cover-2 .c-pub{position:absolute;left:0;top:62px;width:144px;text-align:center;font-size:7.5px;color:#eee;text-transform:uppercase}
.cover-3{left:407px;background:linear-gradient(160deg,#1e3f4a 0%,#2d6c74 40%,#3a8488 60%,#17303a 100%)}
.cover-4{left:571px;background:linear-gradient(#e6d233 0%,#cdb424 35%,#6d621a 60%,#1c1a14 100%)}
.quick{left:116px;top:738px;width:72px;height:23px;background:var(--navy);color:#fff;font-family:'Open Sans',Arial,sans-serif;font-size:10.5px;line-height:23px;text-align:center}
.badge{width:44px;height:44px;border-radius:50%;border:2px solid #fff;color:#fff;font-size:13px;font-style:italic;text-align:center;line-height:40px;box-shadow:0 0 0 1px rgba(0,0,0,.15)}
.badge.new{left:190px;top:638px;background:var(--orange)}
.badge.hot{left:353px;top:638px;background:var(--red)}
.ptitle{top:862px;width:170px;text-align:center;font-size:12px;line-height:15px;color:#444}
.ptitle.lead{color:var(--navy)}
.price{top:900px;width:170px;text-align:center;font-size:11.5px;color:#222}
.price.lead{color:var(--navy)}
.arrow{top:740px}

/* footer */
.footer{left:0;top:932px;width:798px;height:212px;background:var(--footer-bg)}
.fhead{top:22px;font-size:12.5px;text-transform:uppercase;color:#444;padding-bottom:8px;border-bottom:1px solid #d8d8d8}
.flist{list-style:none;font-size:9.5px;color:#444}
.flist li{height:26.5px}
.flist li::before{content:"»";margin-right:8px;color:#444}
.flist.nav-links li:first-child{color:var(--navy)}
.news{width:230px}
.news-item{display:flex;gap:8px;height:49px}
.thumb{width:50px;height:42px;border:2px solid #fff;background:linear-gradient(#d8c9bd,#9a8b80);box-shadow:0 0 0 1px #ddd}
.news-item h4{font-weight:400;font-size:12px;color:var(--navy);line-height:14px}
.news-item p{font-size:9.5px;color:#444;line-height:12px}
.contact{font-size:9.5px;color:#333;line-height:12.5px}
.contact .row{display:flex;gap:8px;align-items:flex-start}
.social{display:flex;gap:8px}
.social span{width:26px;height:26px;border-radius:50%;border:2px solid #c9c9c9}
.social span.on{background:#1f4fb4;border-color:#1f4fb4}

/* bottom bar */
.bottom{left:0;top:1144px;width:798px;height:56px;background:var(--navy)}
.copy{left:84px;top:20px;color:#fff;font-family:'Open Sans',Arial,sans-serif;font-size:9.5px}
.bottom-mark{left:40px;top:14px;width:28px;height:28px;border-radius:50%;background:#3554a8}
.cards{right:40px;top:18px;display:flex;gap:5px}
.cards span{width:28px;height:19px;background:#f2f2f2;border-radius:2px;font-family:'Open Sans',Arial,sans-serif;font-size:6px;font-weight:600;color:#333;text-align:center;line-height:19px;white-space:nowrap;overflow:hidden}
</style>
</head>
<body>

<header>
  <div class="abs search">Search
    <svg width="16" height="16" viewBox="0 0 16 16"><circle cx="6.5" cy="6.5" r="5" fill="none" stroke="#0d2a7a" stroke-width="1.6"/><line x1="10.2" y1="10.2" x2="15" y2="15" stroke="#0d2a7a" stroke-width="1.8"/></svg>
  </div>
  <div class="abs brand">
    <span class="brand-mark"></span>
    <div class="brand-name">BrightOakly.com</div>
    <div class="brand-tag">Predicting and Providing Business and Law Solutions for Multinational Corporations</div>
  </div>
  <div class="abs cart">Shoping cart
    <svg width="22" height="30" viewBox="0 0 22 30"><path d="M6 10V6a5 5 0 0 1 10 0" fill="none" stroke="#0d2a7a" stroke-width="2"/><rect x="1" y="10" width="20" height="19" rx="2" fill="#0d2a7a"/><circle cx="9" cy="21" r="3.5" fill="#fff"/></svg>
  </div>
</header>

<nav class="abs nav">
  <ul>
    <li class="active">Home</li><li>Catlog</li><li>Blog</li><li>About Us</li><li>Doing Business Guides</li><li>Contact Us</li>
  </ul>
</nav>

<section class="abs hero">
  <div class="abs hero-photo" role="img" aria-label="Photo of a smiling young woman in a red top with earphones, leaning on a desk beside an open book"></div>
  <h1 class="abs">Welcome To Bright Oakly</h1>
  <p class="abs">Predicting Providing Business and Law<br>Solutions for Multinational Corportions</p>
  <svg class="abs hero-btn" width="28" height="28" viewBox="0 0 28 28"><circle cx="14" cy="14" r="14" fill="#0d2a7a"/><path d="M12 9l5 5-5 5" fill="none" stroke="#fff" stroke-width="2.4"/></svg>
</section>

<div class="abs tabs">
  <span class="abs tab active" style="left:265px">Featured</span>
  <span class="abs tab" style="left:364px">Best Sellers</span>
  <span class="abs tab" style="left:472px">Popular</span>
</div>

<section>
  <svg class="abs arrow" style="left:47px" width="28" height="28" viewBox="0 0 28 28"><circle cx="14" cy="14" r="14" fill="#7d7d7d"/><path d="M16 9l-5 5 5 5" fill="none" stroke="#fff" stroke-width="2.4"/></svg>
  <svg class="abs arrow" style="left:722px" width="28" height="28" viewBox="0 0 28 28"><circle cx="14" cy="14" r="14" fill="#0d2a7a"/><path d="M12 9l5 5-5 5" fill="none" stroke="#fff" stroke-width="2.4"/></svg>

  <div class="abs cover cover-1" role="img" aria-label="Book cover with a cargo ship at sea">
    <div class="c-title">Silver<br>Pathways and<br>Quarterly Ledger Craft</div>
    <div class="c-author">Elmer T. Vasko</div>
  </div>
  <div class="abs quick">Quick Shop</div>
  <div class="abs cover cover-2" role="img" aria-label="Book cover in white and black">
    <div class="c-band">Expert Field Series</div>
    <div class="c-title">Navigating Levy Matters<br>in Cross-Border<br>Trade</div>
    <div class="c-dark"></div>
    <div class="c-pub" style="top:138px">Lantern House</div>
  </div>
  <div class="abs cover cover-3" role="img" aria-label="Movie poster artwork with a group of young characters"></div>
  <div class="abs cover cover-4" role="img" aria-label="Novel cover with a figure silhouetted against a yellow sky"></div>
  <div class="abs badge new">New</div>
  <div class="abs badge hot">Hot</div>

  <div class="abs ptitle lead" style="left:70px">Silver Pathways and Quarterly Ledger Craft</div>
  <div class="abs ptitle" style="left:233px">Navigating Levy Matters in Cross-Border Trade</div>
  <div class="abs ptitle" style="left:394px">Lorem Ispum dolar consectetur adipiscing</div>
  <div class="abs ptitle" style="left:558px">Nam vitae iaculis mag Quisque fringilla miid</div>
  <div class="abs price lead" style="left:70px">$ 195.00</div>
  <div class="abs price" style="left:233px">$ 120.00</div>
  <div class="abs price" style="left:394px">$ 70.00</div>
  <div class="abs price" style="left:558px">$ 125.00</div>
</section>

<footer class="abs footer">
  <div class="abs fhead" style="left:40px;width:140px">Nevigation</div>
  <ul class="abs flist nav-links" style="left:40px;top:52px">
    <li>Home</li><li>Catlog</li><li>Blog</li><li>About us</li><li>Doing Business Guide</li><li>Contact</li>
  </ul>

  <div class="abs fhead" style="left:207px;width:200px">Latest News</div>
  <div class="abs news" style="left:208px;top:50px">
    <div class="news-item"><div class="thumb" role="img" aria-label="Portrait photo"></div><div><h4>Lorem ipsum dolor</h4><p>Donec nec dignissim lore<br>Vestib ulum lesuada ac a</p></div></div>
    <div class="news-item"><div class="thumb" role="img" aria-label="Portrait photo"></div><div><h4>Lorem ipsum dolor</h4><p>Donec nec dignissim lore<br>Vestib ulum lesuada ac a</p></div></div>
    <div class="news-item"><div class="thumb" role="img" aria-label="Portrait photo"></div><div><h4>Lorem ipsum dolor</h4><p>Donec nec dignissim lore<br>Vestib ulum lesuada ac a</p></div></div>
  </div>

  <div class="abs fhead" style="left:442px;width:125px">Quick Links</div>
  <ul class="abs flist" style="left:442px;top:52px">
    <li>Customer Service</li><li>Search Terms</li><li>Return Policy</li><li>Shipping Policy</li><li>Grow Bussiness</li><li>Sale Information</li>
  </ul>

  <div class="abs fhead" style="left:598px;width:160px">Get in Touch</div>
  <div class="abs contact" style="left:598px;top:52px">
    <div class="row"><svg width="14" height="16" viewBox="0 0 14 16"><path d="M7 1a4 4 0 0 1 4 4c0 3-4 7-4 7S3 8 3 5a4 4 0 0 1 4-4z" fill="none" stroke="#222" stroke-width="1.4"/><path d="M1 15h12" stroke="#222" stroke-width="1.4"/></svg><span>1234 street name, City Name,<br>States Name</span></div>
    <div class="row" style="margin-top:14px"><svg width="14" height="14" viewBox="0 0 14 14"><path d="M3 1l2.5 3-1.5 1.5c1 2 2.5 3.5 4.5 4.5L10 8.5l3 2.5-1.5 2C7 13 1 7 1 2.5z" fill="#222"/></svg><span>123.456.7890</span></div>
    <div class="row" style="margin-top:20px"><svg width="14" height="12" viewBox="0 0 14 12"><rect x="1" y="1" width="12" height="10" fill="none" stroke="#222" stroke-width="1.4"/><path d="M1 1l6 5 6-5" fill="none" stroke="#222" stroke-width="1.4"/></svg><span>info@brightoakly.com</span></div>
    <div class="social" style="margin-top:20px"><span class="on"></span><span></span><span></span><span></span><span></span></div>
  </div>
</footer>

<div class="abs bottom">
  <span class="abs bottom-mark"></span>
  <div class="abs copy">Copyright © 2014 Bright Oakly &nbsp;| All rights reserved.</div>
  <div class="abs cards"><span>Corda</span><span>Vela</span><span>Amber</span><span>Mosto</span><span>Cirra</span><span>PayLark</span></div>
</div>

</body>
</html>
```